Zorv-eL Salsa Website

Needing a website to promote and sell our salsa line.

Each tab at the top of our home page will be need to be clickable taking you to another page. Other pages besides the home page include: about us, recipes, buy now, events, contact us.

Coding

Coded - Design and coding required

Number of Pages Required

5+ page

Requirements
Must have
• Follow us on plain square shape and plain square shape.

Buy now page will need to have option to add products to shopping chart. We have a SumUp account that will need to linked to shopping chart for payments.

```html
<!DOCTYPE html>
<html lang="en">
<head>
<meta charset="utf-8">
<title>Zorv-eL Salsa</title>
<link href="https://fonts.googleapis.com/css2?family=Montserrat:wght@500;600;700&family=Karla:wght@400;500;600&family=Poppins:wght@600;700&display=swap" rel="stylesheet">
<style>
:root{
  --black:#0d0d0d;
  --yellow:#e8b93c;
  --blue:#3b73c2;
  --blue-deep:#2f62b0;
  --red:#b51f24;
  --ink:#1c1c1c;
  --muted:#555;
  --line:#dedede;
  --white:#fff;
}
*{box-sizing:border-box;margin:0;padding:0}
html,body{width:1200px;height:3499px;overflow:hidden}
body{position:relative;background:var(--white);font-family:"Karla",sans-serif;color:var(--ink)}
.abs{position:absolute}
.header{left:0;top:0;width:1200px;height:98px;background:var(--black)}
.brand{left:98px;top:28px;display:flex;align-items:center;gap:10px;font-family:"Montserrat",sans-serif;font-weight:700;font-size:26px;color:var(--yellow)}
.brand .dot{width:16px;height:16px;background:var(--red);border-radius:50%}
.header-icons{right:100px;top:34px;display:flex;gap:28px}
.header-icons svg{width:28px;height:28px;stroke:var(--white);fill:none;stroke-width:2}
.nav{left:0;top:98px;width:1200px;height:45px;background:var(--yellow);display:flex;align-items:center;padding-left:177px}
.nav a{font-family:"Montserrat",sans-serif;font-weight:600;font-size:16px;color:var(--white);text-decoration:none;width:162px}
.hero{left:0;top:143px;width:1200px;height:600px;overflow:hidden}
.hero-bg{left:0;top:0;width:1200px;height:600px;background:linear-gradient(90deg,#2a211c,#4a3a30 50%,#2a211c)}
.hero-circle{left:231px;top:20px;width:740px;height:740px;border-radius:50%;background:var(--blue)}
.hero-jars{left:262px;top:220px;width:660px;height:380px;background:radial-gradient(ellipse at center,#8c1a14 0%,#5a120f 60%,#2a0c0a 100%);border-radius:60px 60px 40px 40px}
.hero-title{left:0;top:88px;width:1200px;text-align:center;font-family:"Poppins",sans-serif;font-weight:700;font-size:66px;color:var(--white)}
.arrow{top:274px;width:40px;height:40px;border:2.5px solid var(--white);border-radius:50%;display:flex;align-items:center;justify-content:center}
.arrow svg{width:18px;height:18px;fill:var(--white)}
.section-title{left:0;width:1200px;text-align:center;font-family:"Montserrat",sans-serif;font-weight:700;font-size:42px;color:var(--ink)}
.card{border:1px solid var(--line);background:var(--white)}
.card .jar{position:absolute;left:50%;top:18px;transform:translateX(-50%);width:200px;height:278px;border-radius:30px 30px 50px 50px;background:linear-gradient(180deg,#1a1a1a 0 18%,#8e1b14 18% 100%)}
.card-name{text-align:center;font-family:"Montserrat",sans-serif;font-weight:600;font-size:18px}
.price{text-align:center;font-family:"Karla",sans-serif;font-size:19px;color:var(--blue)}
.deal-photo{left:91px;top:1370px;width:484px;height:484px;border-radius:50%;border:3px solid var(--blue);background:linear-gradient(160deg,#6f8a5a 0%,#3a3a3a 40%,#b7413a 75%,#2b57a5 100%)}
.deal-title{left:722px;top:1496px;font-family:"Montserrat",sans-serif;font-weight:700;font-size:44px;color:var(--white)}
.deal-text{left:722px;top:1577px;font-size:26px;line-height:35px;color:var(--white);font-weight:500}
.deal-text small{font-size:10px;margin-left:14px}
.btn{left:722px;top:1692px;width:155px;height:48px;border-radius:24px;background:var(--blue);color:var(--white);font-size:17px;display:flex;align-items:center;justify-content:center}
.tile{background:linear-gradient(160deg,#7a6a5e,#3b2a22)}
.divider{left:90px;top:2458px;width:1020px;height:1px;background:var(--line)}
.stars{left:0;top:2592px;width:1200px;text-align:center;color:var(--yellow);font-size:18px;letter-spacing:6px}
.quote{left:130px;top:2628px;width:940px;text-align:center;font-size:17px;line-height:27px;color:var(--muted)}
.avatar{border-radius:50%;background:radial-gradient(circle at 50% 40%,#d9c9d6,#b9a8b8)}
.reviewer{left:0;top:2838px;width:1200px;text-align:center;font-size:17px;color:var(--muted)}
.footer{left:0;top:2960px;width:1200px;height:539px;background:var(--black)}
.feature{top:3078px;display:flex;align-items:center;gap:14px;color:var(--white);font-size:14px;line-height:22px}
.feature .ic{width:56px;height:56px;border:2px solid var(--white);border-radius:50%;display:flex;align-items:center;justify-content:center}
.feature .ic svg{width:24px;height:24px;fill:var(--white)}
.foot-rule{left:90px;top:3178px;width:1020px;height:1px;background:#2a2a2a}
.foot-head{top:3212px;font-family:"Montserrat",sans-serif;font-weight:500;font-size:21px;color:var(--white)}
.foot-links{font-size:11px;font-weight:600;color:var(--white);line-height:30px;text-transform:uppercase}
.contact{left:597px;top:3262px;font-size:11px;color:var(--white);line-height:27px}
.contact span.i{display:inline-block;width:10px;height:10px;background:var(--white);border-radius:2px;margin-right:5px;vertical-align:-1px}
.social{left:391px;top:3266px;display:flex;gap:20px}
.social span{width:14px;height:14px;background:var(--white);border-radius:2px}
.email-box{left:824px;top:3270px;width:284px;height:44px;border:1px solid var(--white);color:var(--white);font-size:11px;padding-left:20px;display:flex;align-items:center}
.signup{left:824px;top:3330px;width:284px;height:44px;background:var(--blue-deep);color:var(--white);font-size:17px;font-weight:600;display:flex;align-items:center;justify-content:center}
.copyright{left:88px;top:3456px;font-size:11px;color:var(--white)}
.cards{left:940px;top:3450px;display:flex;gap:8px}
.cards span{width:46px;height:24px;border-radius:3px;background:#e6e6e6}
.cards span:nth-child(2){background:#d8d8d8}
.cards span:nth-child(3){background:#cfd8e6}
.cards span:nth-child(4){width:24px;background:#bcd0ea}
</style>
</head>
<body>

<header class="abs header">
  <div class="abs brand"><span class="dot"></span>Zorv-eL Salsa</div>
  <div class="abs header-icons">
    <svg viewBox="0 0 24 24"><path d="M12 20s-7-4.5-7-10a4 4 0 0 1 7-2.5A4 4 0 0 1 19 10c0 5.5-7 10-7 10z"/></svg>
    <svg viewBox="0 0 24 24"><path d="M5 8h14l-1 12H6z"/><path d="M9 8V6a3 3 0 0 1 6 0v2"/></svg>
    <svg viewBox="0 0 24 24"><circle cx="12" cy="8" r="4"/><path d="M4 21c1-4 4-6 8-6s7 2 8 6z"/></svg>
    <svg viewBox="0 0 24 24"><rect x="3" y="5" width="18" height="14" rx="2"/><path d="M3 7l9 6 9-6"/></svg>
  </div>
</header>

<nav class="abs nav">
  <a href="#">Home</a><a href="#">About Us</a><a href="#">Recipes</a><a href="#">Buy Now</a><a href="#">Events</a><a href="#">Contact Us</a>
</nav>

<section class="abs hero">
  <div class="abs hero-bg" role="img" aria-label="Blurred photo of salsa jars on a wooden table"></div>
  <div class="abs hero-circle"></div>
  <div class="abs hero-jars" role="img" aria-label="Photo of three salsa jars: mild, medium and hot"></div>
  <h1 class="abs hero-title">ZorvEl Salsa</h1>
  <div class="abs arrow" style="left:23px"><svg viewBox="0 0 20 20"><path d="M14 3L5 10l9 7z"/></svg></div>
  <div class="abs arrow" style="left:1133px"><svg viewBox="0 0 20 20"><path d="M6 3l9 7-9 7z"/></svg></div>
  <svg class="abs" style="left:0;top:500px" width="1200" height="100" viewBox="0 0 1200 100" preserveAspectRatio="none">
    <path d="M0 60 C300 30 700 120 1200 40 L1200 100 L0 100z" fill="#fff"/>
    <path d="M40 62 C250 80 450 78 700 70 C500 92 250 90 40 62z" fill="#2f62b0"/>
  </svg>
</section>

<h2 class="abs section-title" style="top:828px">Featured Products</h2>
<div class="abs card" style="left:90px;top:897px;width:328px;height:312px"><div class="jar" role="img" aria-label="Mild salsa jar photo"></div></div>
<div class="abs card" style="left:436px;top:897px;width:328px;height:312px"><div class="jar" role="img" aria-label="Hot salsa jar photo"></div></div>
<div class="abs card" style="left:782px;top:897px;width:328px;height:312px"><div class="jar" role="img" aria-label="Medium salsa jar photo"></div></div>
<div class="abs card-name" style="left:90px;top:1236px;width:328px">ZorvEl Salsa Mild</div>
<div class="abs card-name" style="left:436px;top:1236px;width:328px">ZorvEl Salsa Hot</div>
<div class="abs card-name" style="left:782px;top:1236px;width:328px">ZorvEl Salsa Medium</div>

<svg class="abs" style="left:0;top:1370px" width="1200" height="482" viewBox="0 0 1200 482" preserveAspectRatio="none">
  <path d="M0 30 C200 90 300 170 560 100 C800 40 1000 10 1200 10 L1200 482 C1000 470 800 440 600 420 C400 400 200 410 0 460z" fill="#b51f24"/>
</svg>
<div class="abs deal-photo" role="img" aria-label="Photo of a salsa tasting booth at an outdoor market"></div>
<div class="abs deal-title">Best Deal</div>
<div class="abs deal-text">Get 25% Off <small>Or</small><br>Buy 1 Get One Free</div>
<div class="abs btn">Shop Now</div>

<h2 class="abs section-title" style="top:1953px">Products</h2>
<div class="abs card" style="left:90px;top:2029px;width:243px;height:289px"><div class="jar" role="img" aria-label="Salsa jar photo" style="width:170px;height:250px"></div></div>
<div class="abs tile" style="left:349px;top:2029px;width:243px;height:289px" role="img" aria-label="Photo of salsa jar with tacos"></div>
<div class="abs tile" style="left:608px;top:2029px;width:243px;height:289px;background:linear-gradient(160deg,#5a2a20,#2a1410)" role="img" aria-label="Photo of many stacked salsa jars"></div>
<div class="abs tile" style="left:867px;top:2029px;width:243px;height:289px;background:linear-gradient(160deg,#8a6a4c,#3a2a20)" role="img" aria-label="Photo of a hand holding a salsa jar"></div>
<div class="abs card-name" style="left:90px;top:2333px;width:243px">ZorvEl Salsa</div>
<div class="abs card-name" style="left:349px;top:2333px;width:243px">ZorvEl Salsa</div>
<div class="abs card-name" style="left:608px;top:2333px;width:243px">ZorvEl Salsa</div>
<div class="abs card-name" style="left:867px;top:2333px;width:243px">ZorvEl Salsa</div>
<div class="abs price" style="left:90px;top:2363px;width:243px">$59.95</div>
<div class="abs price" style="left:349px;top:2363px;width:243px">$110</div>
<div class="abs price" style="left:608px;top:2363px;width:243px">$110</div>
<div class="abs price" style="left:867px;top:2363px;width:243px">$150</div>
<div class="abs divider"></div>

<h2 class="abs section-title" style="top:2514px">Testimonials</h2>
<div class="abs stars">★★★★★</div>
<p class="abs quote">Lorem ipsum dolor sit amet, consectetur adipiscing elit, sed do eiusmod tempor incididunt ut labore et dolore magna aliqua. Ut enim ad minim veniam, quis nostrud exerco laboris nisnsequat.</p>
<div class="abs avatar" style="left:401px;top:2720px;width:94px;height:94px" role="img" aria-label="Customer portrait"></div>
<div class="abs avatar" style="left:543px;top:2710px;width:112px;height:112px;background:radial-gradient(circle at 50% 40%,#a07a66,#4a2e24)" role="img" aria-label="Customer portrait"></div>
<div class="abs avatar" style="left:704px;top:2720px;width:94px;height:94px" role="img" aria-label="Customer portrait"></div>
<div class="abs reviewer">Marla T., Oakridge, US</div>

<svg class="abs" style="left:0;top:2940px" width="1200" height="80" viewBox="0 0 1200 80" preserveAspectRatio="none">
  <path d="M0 40 C300 -10 600 60 1200 0 L1200 80 L0 80z" fill="#0d0d0d"/>
  <path d="M0 38 C30 28 60 24 80 24 C40 30 20 34 0 38z M600 50 C800 30 1000 22 1150 30 C950 30 780 40 600 50z" fill="#3b73c2"/>
</svg>
<footer class="abs footer"></footer>

<div class="abs feature" style="left:92px"><div class="ic"><svg viewBox="0 0 24 24"><path d="M12 4a8 8 0 0 1 7.7 6h-2.1A6 6 0 0 0 7 8.5L9.5 11H3V4.5l2.5 2.5A8 8 0 0 1 12 4zm0 16a8 8 0 0 1-7.7-6h2.1A6 6 0 0 0 17 15.5L14.5 13H21v6.5L18.5 17A8 8 0 0 1 12 20z"/></svg></div><div>90 days return<br>3 days for free return</div></div>
<div class="abs feature" style="left:351px"><div class="ic"><svg viewBox="0 0 24 24"><path d="M2 6h12v10H2zM14 9h4l3 4v3h-7z"/><circle cx="6" cy="18" r="2"/><circle cx="17" cy="18" r="2"/></svg></div><div>Free Shipping<br>Free shipping on order</div></div>
<div class="abs feature" style="left:621px"><div class="ic"><svg viewBox="0 0 24 24"><path d="M21 3L2 11l6 2 2 7 3-5 5 4z"/></svg></div><div>Proffesional Support<br>Call : 866-555-0142</div></div>
<div class="abs feature" style="left:881px"><div class="ic"><svg viewBox="0 0 24 24"><path d="M3 9h18v4H3zM5 13h14v8H5z"/><rect x="11" y="9" width="2" height="12" fill="#0d0d0d"/></svg></div><div>Gift Card<br>Gift Card On Purchase</div></div>
<div class="abs foot-rule"></div>

<div class="abs foot-head" style="left:89px">Main menu</div>
<div class="abs foot-links" style="left:91px;top:3252px">Home<br>About Us<br>Recipes<br>Buy Now</div>
<div class="abs foot-links" style="left:224px;top:3252px">Events<br>Contact Us</div>
<div class="abs foot-head" style="left:389px">Stay In Touch</div>
<div class="abs social" aria-label="Social links"><span></span><span></span></div>
<div class="abs foot-head" style="left:597px">Contact Us</div>
<div class="abs contact">214 BRENNAN AVE #3 ASHFORD,<br>VA 24000 USA<br><span class="i"></span>+1 913-555-0187<br><span class="i"></span>HELLO@ZORVELSALSA.COM</div>
<div class="abs foot-head" style="left:824px">News &amp; updates</div>
<div class="abs email-box">Enter Your Email address</div>
<div class="abs signup">Sign Up</div>
<div class="abs copyright">© Copyrights.2021.The Company Name.All Rights Reserved</div>
<div class="abs cards" aria-label="Accepted payment cards"><span></span><span></span><span></span><span></span></div>

</body>
</html>
```